Simple Recipe eBook

I need the graphic work done for a simple recipe ebook, I have attached all of the required information for it, as well as our company logo. Further company info can be found at velorique.com

I would like each recipe page to include 2 recipes, each recipe needs to include ingredients, picture, method, and nutritional info.

I would like the style to appear fresh and healthy, with lots of graphics and colours to match.
Please let me know if you need any guidance

Target Market(s)

Females aged from 15-25

Industry/Entity Type

It Company

```html
<!DOCTYPE html>
<html lang="en">
<head>
<meta charset="utf-8">
<title>Velorique Detox and Diet Guide</title>
<link rel="stylesheet" href="https://fonts.googleapis.com/css2?family=Quicksand:wght@400;500;600;700&display=swap">
<style>
  :root {
    --teal: #3fc3c9;
    --ink: #4b4b4b;
    --text: #555555;
    --muted: #8a8a8a;
    --rule: #cfcfcf;
    --page-edge: #1f1f1f;
    --paper: #ffffff;
    --canvas: #ffffff;
  }
  * { box-sizing: border-box; margin: 0; padding: 0; }
  html, body { width: 1200px; height: 1000px; overflow: hidden; background: var(--canvas); }
  body { position: relative; font-family: "Quicksand", sans-serif; color: var(--text); }

  .page {
    position: absolute; width: 326px; height: 460px;
    background: var(--paper); border: 1px solid var(--page-edge); overflow: hidden;
  }
  .col-1 { left: 105px; } .col-2 { left: 437px; } .col-3 { left: 769px; }
  .row-1 { top: 38px; } .row-2 { top: 504px; }

  .abs { position: absolute; }

  /* cover */
  .brand-name { left: 0; width: 100%; text-align: center; font-weight: 500; color: var(--ink); }
  .cover .brand-name { top: 186px; font-size: 30px; letter-spacing: 1.5px; }
  .intro .brand-name { top: 134px; font-size: 16px; letter-spacing: 1px; }
  .guide-title { top: 292px; left: 0; width: 100%; text-align: center; font-size: 13px; color: var(--teal); }
  .contacts { top: 358px; left: 0; width: 100%; text-align: center; font-size: 6.5px; line-height: 1.45; color: var(--ink); }

  /* intro */
  .intro-copy { left: 68px; top: 190px; width: 200px; font-size: 5.4px; line-height: 1.5; color: var(--text); }
  .intro-copy p { margin-bottom: 6px; }
  .intro-copy strong { font-weight: 700; }
  .ready { left: 68px; top: 282px; font-size: 6.5px; font-weight: 700; line-height: 1.4; color: var(--teal); }

  /* dos & donts */
  .badge {
    left: 148px; width: 30px; height: 30px; border-radius: 50%; background: var(--teal);
    color: #fff; font-size: 5.5px; font-weight: 700; display: flex; align-items: center; justify-content: center;
  }
  .tips { left: 46px; width: 240px; font-size: 4.6px; line-height: 1.45; color: var(--text); }
  .tips p { margin-bottom: 6px; }
  .tips b { color: var(--teal); font-weight: 700; }

  /* recipe pages */
  .section-title { left: 20px; top: 18px; font-size: 11px; font-weight: 700; letter-spacing: 0.8px; color: var(--teal); }
  .photo { border-radius: 1px; }
  .recipe-name { font-size: 5.8px; font-weight: 700; color: var(--teal); }
  .ingredients { font-size: 4.8px; line-height: 1.4; color: var(--text); list-style: none; font-style: italic; }
  .method { font-size: 4.8px; line-height: 1.5; color: var(--text); }
  .method p { margin-bottom: 6px; }
  .divider { left: 20px; width: 286px; border-top: 1px dashed var(--rule); }

  .nutrition { width: 120px; }
  .nutrition h4 { font-size: 6px; font-weight: 500; color: var(--muted); margin-bottom: 5px; }
  .nutrition dl { display: grid; grid-template-columns: 1fr 1fr; column-gap: 10px; row-gap: 3px; }
  .nutrition dl div { font-size: 3.8px; line-height: 1.25; color: var(--muted); }
  .nutrition dd { color: var(--muted); }
  .nutrition .note { margin-top: 5px; font-size: 3.6px; color: var(--muted); }
</style>
</head>
<body>

<!-- Cover -->
<section class="page col-1 row-1 cover">
  <div class="abs brand-name">VELORIQUE</div>
  <div class="abs guide-title">Detox and Diet Guide</div>
  <div class="abs contacts">velorique.com<br>fb.com/velorique<br>instagram.com/velorique</div>
</section>

<!-- Intro -->
<section class="page col-2 row-1 intro">
  <div class="abs brand-name">VELORIQUE</div>
  <div class="abs intro-copy">
    <p>At <strong>Velorique</strong> we want to help you be the best you can be!</p>
    <p>That's why we have put together this simple guide to motivate, inspire, inform and help you reach your goals.</p>
    <p>Below you will find a collection of healthy and easy recipe ideas and tips to kickstart your detox and diet journey.</p>
  </div>
  <div class="abs ready">Ready?<br>Set...<br>GO!</div>
</section>

<!-- Dos and Donts -->
<section class="page col-3 row-1 tips-page">
  <div class="abs badge" style="top:20px;">DOS</div>
  <div class="abs tips" style="top:62px;">
    <p><b>EXERCISE!</b> Exercise is the key to achieving your goals. Aim for at least 30 minutes of high intensity cardio or weight training each day.</p>
    <p><b>COUNT YOUR CALORIES!</b> To be sure you aren't eating too much you should make sure to count your calories. Download an app like CalorieNote to help you keep track on the go. The app will also help decide how many calories you should be consuming per day.</p>
    <p><b>DRINK PLENTY OF WATER!</b> Staying hydrated is important to keep your body functioning at its peak. A glass of water before each meal can help you feel fuller quicker. It also helps flush nasty toxins.</p>
    <p><b>GET A GOOD NIGHTS SLEEP!</b> Your beauty rest is important to help your body repair. 6-8 hours every night is recommended.</p>
    <p><b>WRITE DOWN YOUR GOALS!</b> Did you know that writing down your goals increases your chance of actually completing them? Give it a go. Write them down and stick to them. Hard work and consistency pays off!</p>
    <p><b>EAT FRUITS AND VEGES!</b> Fresh fruit and veges are loaded with healthy vitamins and antioxidants that your body loves!</p>
    <p><b>DO IT WITH A FRIEND!</b> Doing your diet and detox with a friend can be a great way to boost motivation and get results. Keep each other on track and share ideas!</p>
  </div>
  <div class="abs badge" style="top:238px;">DONTS</div>
  <div class="abs tips" style="top:280px;">
    <p><b>CHEAT!</b> Eating something bad or skipping a workout every now and then is ok, but don't make a habit of it. At the end of the day you are only hurting yourself.</p>
    <p><b>FAST FOOD!</b> Highly processed, fatty and sugar loaded fast food options can be very bad for you! If you do choose to eat out, make sure to have a good look at the nutritional information, especially the total calories.</p>
    <p><b>AVOID FATS!</b> Despite what you might have heard, fats don't make you fat! Healthy fats are essential to keep your body functioning. Good fat sources include salmon, avocado, and fish oil supplements.</p>
    <p><b>ALCOHOL!</b> A glass of red wine every now and then can actually be beneficial for you, but drinking to excess can seriously damage your progress and ruin your detox! Did you know that one vodka and raspberry drink can contain over 200 calories? Ouch!</p>
    <p><b>SALAD DRESSINGS AND SAUCES!</b> Salads are a great option, but be careful when choosing the dressing. Some sauces and dressings can be very high in calories.</p>
    <p><b>QUIT!</b> Don't quit! It might seem hard, but you will thank yourself in the long run!</p>
  </div>
</section>

<!-- Breakfast -->
<section class="page col-1 row-2 recipes">
  <div class="abs section-title">BREAKFAST</div>
  <div class="abs photo" role="img" aria-label="Photo of pesto scrambled eggs with spinach and avocado on toast" style="left:22px;top:47px;width:142px;height:80px;background:linear-gradient(135deg,#c9d7c3,#e6d79a 45%,#8faa6e);"></div>
  <div class="abs recipe-name" style="left:22px;top:162px;">Pesto scrambled eggs with spinach &amp; avocado</div>
  <ul class="abs ingredients" style="left:22px;top:180px;width:140px;">
    <li>4 eggs</li><li>2 tablespoons milk</li><li>75g baby spinach leaves</li>
    <li>1 tablespoon basil pesto, plus extra to serve</li><li>Olive oil spray</li>
    <li>1/2 large firm ripe avocado, stone removed, chopped</li><li>2 slices wholegrain toast, to serve</li>
  </ul>
  <div class="abs method" style="left:179px;top:20px;width:128px;">
    <p>Whisk the eggs and milk together in a medium size bowl. Season with salt and pepper. Heat a medium size frying pan over a medium heat and spray lightly with olive oil spray.</p>
    <p>Add the baby spinach leaves. Cook, stirring, until just wilted. Remove from pan.</p>
    <p>Return pan to a medium heat, spray with a little more oil. Add egg mixture and using a wooden spoon, stir and bring the egg mixture on the edge of the pan to the centre. Continue until the eggs are almost set. Add the pesto and baby spinach, and stir until just combined. Season to taste with sea salt and freshly ground black pepper. Serve immediately with toast, chopped avocado and an extra dollop of pesto if desired.</p>
  </div>
  <div class="abs nutrition" style="left:179px;top:160px;">
    <h4>Nutrition</h4>
    <dl>
      <div><dt>Energy</dt><dd>1446kJ</dd></div><div><dt>Dietary Fibre</dt><dd>5.0g</dd></div>
      <div><dt>Fat saturated</dt><dd>5.2g</dd></div><div><dt>Protein</dt><dd>19.4g</dd></div>
      <div><dt>Fat Total</dt><dd>22.1g</dd></div><div><dt>Cholesterol</dt><dd>378mg</dd></div>
      <div><dt>Carbohydrate sugars</dt><dd>2.1g</dd></div><div><dt>Sodium</dt><dd>412mg</dd></div>
      <div><dt>Carbohydrate Total</dt><dd>16.3g</dd></div>
    </dl>
    <p class="note">All nutrition values are per serve.</p>
  </div>
  <div class="abs divider" style="top:236px;"></div>
  <div class="abs photo" role="img" aria-label="Photo of a green power smoothie in a glass with a striped straw" style="left:22px;top:257px;width:142px;height:96px;background:linear-gradient(160deg,#e9ece4,#b9c98f 55%,#8ea465);"></div>
  <div class="abs recipe-name" style="left:22px;top:368px;">Power Smoothie</div>
  <ul class="abs ingredients" style="left:22px;top:386px;width:140px;">
    <li>2 large ripe bananas, roughly chopped</li><li>1/2 cup reduced-fat plain yoghurt</li>
    <li>2 tablespoons rolled oats</li><li>1 tablespoon Greenfield Super Greens powder (see note)</li>
    <li>2 teaspoons honey (optional)</li><li>1 1/2 cups reduced-fat milk</li>
  </ul>
  <div class="abs method" style="left:179px;top:262px;width:128px;">
    <p>Blend banana, yoghurt, rolled oats, super greens, honey (if using) and milk together until smooth. Pour into chilled glasses. Serve.</p>
  </div>
  <div class="abs nutrition" style="left:179px;top:340px;">
    <h4>Nutrition</h4>
    <dl>
      <div><dt>Energy</dt><dd>1012kJ</dd></div><div><dt>Dietary Fibre</dt><dd>3.4g</dd></div>
      <div><dt>Fat saturated</dt><dd>1.6g</dd></div><div><dt>Protein</dt><dd>11.2g</dd></div>
      <div><dt>Fat Total</dt><dd>3.1g</dd></div><div><dt>Cholesterol</dt><dd>12mg</dd></div>
      <div><dt>Carbohydrate sugars</dt><dd>31.5g</dd></div><div><dt>Sodium</dt><dd>118mg</dd></div>
      <div><dt>Carbohydrate Total</dt><dd>42.7g</dd></div>
    </dl>
    <p class="note">All nutrition values are per serve.</p>
  </div>
</section>

<!-- Breakfast continued -->
<section class="page col-2 row-2 recipes">
  <div class="abs photo" role="img" aria-label="Photo of two jars of green breakfast smoothie with straws" style="left:25px;top:23px;width:143px;height:75px;background:linear-gradient(160deg,#eef0ea,#bdd39a 60%,#9fbb74);"></div>
  <div class="abs recipe-name" style="left:25px;top:137px;">Green Breakfast Smoothie</div>
  <ul class="abs ingredients" style="left:25px;top:154px;width:140px;">
    <li>1/2 firm ripe avocado</li><li>1 ripe banana, sliced</li><li>1 kiwifruit, peeled, chopped</li>
    <li>Large handful baby spinach leaves</li><li>375ml (1 1/2 cups) low fat milk</li>
    <li>(cow, soy, almond, rice or coconut)</li><li>1/4 teaspoon ground cinnamon</li>
    <li>2 teaspoons honey</li><li>1/2 cup ice cubes</li>
  </ul>
  <div class="abs method" style="left:184px;top:24px;width:124px;">
    <p>Place all ingredients in a blender and blend until smooth, thick and creamy. Divide between 2 glasses, serve immediately. Tip: try adding a tablespoon of protein powder for long lasting energy throughout the day.</p>
  </div>
  <div class="abs nutrition" style="left:184px;top:92px;">
    <h4>Nutrition</h4>
    <dl>
      <div><dt>Energy</dt><dd>1190kJ</dd></div><div><dt>Dietary Fibre</dt><dd>6.1g</dd></div>
      <div><dt>Fat saturated</dt><dd>3.2g</dd></div><div><dt>Protein</dt><dd>9.8g</dd></div>
      <div><dt>Fat Total</dt><dd>12.4g</dd></div><div><dt>Cholesterol</dt><dd>8mg</dd></div>
      <div><dt>Carbohydrate sugars</dt><dd>28.0g</dd></div><div><dt>Sodium</dt><dd>96mg</dd></div>
      <div><dt>Carbohydrate Total</dt><dd>34.6g</dd></div>
    </dl>
    <p class="note">All nutrition values are per serve.</p>
  </div>
  <div class="abs divider" style="top:226px;"></div>
  <div class="abs photo" role="img" aria-label="Photo of fresh berries in a dish topped with toffeed yoghurt" style="left:25px;top:250px;width:143px;height:94px;background:linear-gradient(135deg,#f3eee6,#e9a45f 40%,#c23a3c 75%,#7d2a3a);"></div>
  <div class="abs recipe-name" style="left:25px;top:358px;">Berries with Toffeed Yoghurt</div>
  <ul class="abs ingredients" style="left:25px;top:375px;width:140px;">
    <li>1/2 cup caster sugar</li><li>250g strawberries, hulled, halved lengthways</li>
    <li>150g blueberries</li><li>120g raspberries</li>
    <li>2 cups Greek-style yoghurt, drained *</li>
  </ul>
  <div class="abs method" style="left:184px;top:248px;width:124px;">
    <p>Make toffee syrup: Place sugar in a heavy based frying pan over medium low heat. Cook, tilting pan back and forth and stirring with a metal spoon for 5 minutes or until sugar dissolves and turns golden.</p>
    <p>Meanwhile, combine berries in a shallow serving dish. Dollop yoghurt over berries. Drizzle with hot toffee syrup. Serve.</p>
    <p>* Draining yoghurt: Yoghurt can be thickened further by removing excess moisture. Spoon yoghurt into a fine mesh sieve. Cover and place over a bowl. Refrigerate for 3 hours.</p>
  </div>
  <div class="abs nutrition" style="left:184px;top:352px;">
    <h4>Nutrition</h4>
    <dl>
      <div><dt>Energy</dt><dd>1085kJ</dd></div><div><dt>Dietary Fibre</dt><dd>3.9g</dd></div>
      <div><dt>Fat saturated</dt><dd>4.5g</dd></div><div><dt>Protein</dt><dd>8.1g</dd></div>
      <div><dt>Fat Total</dt><dd>7.0g</dd></div><div><dt>Cholesterol</dt><dd>22mg</dd></div>
      <div><dt>Carbohydrate sugars</dt><dd>38.9g</dd></div><div><dt>Sodium</dt><dd>74mg</dd></div>
      <div><dt>Carbohydrate Total</dt><dd>40.2g</dd></div>
    </dl>
    <p class="note">All nutrition values are per serve.</p>
  </div>
</section>

<!-- Lunch -->
<section class="page col-3 row-2 recipes">
  <div class="abs section-title">LUNCH</div>
  <div class="abs photo" role="img" aria-label="Photo of chilli garlic prawns served on a plate with rocket" style="left:20px;top:51px;width:143px;height:97px;background:linear-gradient(135deg,#dfe6ea,#e2744d 45%,#b8442f 70%,#6f8d54);"></div>
  <div class="abs recipe-name" style="left:182px;top:28px;">Chilli Garlic Prawns</div>
  <ul class="abs ingredients" style="left:182px;top:45px;width:124px;">
    <li>2 tablespoons olive oil</li><li>60g butter</li><li>4 garlic cloves, thinly sliced lengthways</li>
    <li>2 long fresh red chillies, finely chopped</li><li>1kg peeled green prawns, with tails intact</li>
    <li>2 tablespoons fresh lemon juice</li><li>1 teaspoon grated lemon rind</li>
    <li>1/4 cup chopped fresh coriander</li><li>Rocket leaves, to serve</li>
    <li>Crusty bread, sliced, brushed with oil, chargrilled, to serve</li>
  </ul>
  <div class="abs method" style="left:182px;top:140px;width:124px;">
    <p>Heat the oil and butter in a large frying pan over medium-high heat. Add the garlic and chilli and cook, stirring, for 1 minute or until aromatic. Add the prawns and season with salt and pepper. Cook, stirring, for 3-4 minutes or until the prawns are just cooked through.</p>
    <p>Add the lemon juice, lemon rind and coriander to the prawn mixture and toss to combine. Divide the prawns among serving plates and serve with rocket and bread.</p>
  </div>
  <div class="abs nutrition" style="left:20px;top:158px;">
    <h4>Nutrition</h4>
    <dl>
      <div><dt>Energy</dt><dd>1320kJ</dd></div><div><dt>Dietary Fibre</dt><dd>1.2g</dd></div>
      <div><dt>Fat saturated</dt><dd>8.4g</dd></div><div><dt>Protein</dt><dd>36.5g</dd></div>
      <div><dt>Fat Total</dt><dd>19.8g</dd></div><div><dt>Cholesterol</dt><dd>290mg</dd></div>
      <div><dt>Carbohydrate sugars</dt><dd>0.9g</dd></div><div><dt>Sodium</dt><dd>640mg</dd></div>
      <div><dt>Carbohydrate Total</dt><dd>1.8g</dd></div>
    </dl>
    <p class="note">All nutrition values are per serve.</p>
  </div>
  <div class="abs divider" style="top:240px;"></div>
  <div class="abs photo" role="img" aria-label="Photo of a bowl of crab and corn soup garnished with shallots" style="left:20px;top:260px;width:143px;height:93px;background:linear-gradient(150deg,#eceae2,#d8c27a 55%,#b79a4c);"></div>
  <div class="abs recipe-name" style="left:20px;top:370px;">Crab &amp; Corn Soup</div>
  <ul class="abs ingredients" style="left:20px;top:386px;width:140px;">
    <li>1 x 500g pot sweet corn and chives soup (Harvest Pot brand)</li>
    <li>250ml (1 cup) vegetable stock</li><li>1 x 125g can corn kernels, drained</li>
    <li>2 x 170g cans crab meat, drained</li><li>1 green shallot, ends trimmed, thinly sliced diagonally</li>
    <li>Pinch of salt</li>
  </ul>
  <div class="abs method" style="left:182px;top:262px;width:124px;">
    <p>Combine the soup, stock and corn kernels in a large saucepan over medium-high heat and bring to the boil. Cook, uncovered, for 5 minutes.</p>
    <p>Reduce heat to low and stir in the crab meat and half the shallots. Taste and season with salt.</p>
    <p>Ladle the soup into serving bowls and sprinkle with the remaining shallots.</p>
  </div>
  <div class="abs nutrition" style="left:182px;top:345px;">
    <h4>Nutrition</h4>
    <dl>
      <div><dt>Energy</dt><dd>870kJ</dd></div><div><dt>Dietary Fibre</dt><dd>3.3g</dd></div>
      <div><dt>Fat saturated</dt><dd>0.8g</dd></div><div><dt>Protein</dt><dd>16.7g</dd></div>
      <div><dt>Fat Total</dt><dd>3.5g</dd></div><div><dt>Cholesterol</dt><dd>58mg</dd></div>
      <div><dt>Carbohydrate sugars</dt><dd>6.2g</dd></div><div><dt>Sodium</dt><dd>890mg</dd></div>
      <div><dt>Carbohydrate Total</dt><dd>22.4g</dd></div>
    </dl>
    <p class="note">All nutrition values are per serve.</p>
  </div>
</section>

</body>
</html>
```